Honeyvale Stitchery Needs a Beautiful Website

I need a new website for this new E-commerce. I sell handmade baby crochets, e.g. booties, headbands, hats, etc. I need a feminine and soft design to make the moms-to-be say 'oohh ahh'. I'd like pink, blue and gray. I'd like an inviting homepage, and nice regular pages where people can see and order the products.

Industry/Entity Type

Baby

Requirements
Must have
• beautiful, soft, feminine design. Please use pictures of the colors I'd like: brown, yellow, pink and blue. Any combination, but definitely include brown.

```html
<!DOCTYPE html>
<html lang="en">
<head>
<meta charset="utf-8">
<title>Honeyvale Stitchery</title>
<link href="https://fonts.googleapis.com/css2?family=Open+Sans:wght@400;600;700&family=Pacifico&display=swap" rel="stylesheet">
<style>
:root{
  --page-bg:#fdfbf6;
  --lavender:#a680d6;
  --lavender-dark:#8a62c0;
  --coral:#f96f7c;
  --pink:#e9457a;
  --sky:#72aed0;
  --sky-light:#8cc8ec;
  --sky-text:#5fa6c9;
  --green:#8cc10a;
  --yellow:#fbb90c;
  --red:#ee4156;
  --teal:#1eaac4;
  --ink:#333;
  --white:#fff;
  --line:#e4e4e4;
}
*{margin:0;padding:0;box-sizing:border-box}
html,body{width:737px;height:1200px;overflow:hidden}
body{background:var(--page-bg);font-family:"Open Sans",Arial,sans-serif;position:relative;color:var(--ink)}
.page{position:absolute;left:35px;top:16px;width:668px;height:1156px;background:var(--white)}

/* header */
.header{position:absolute;left:0;top:0;width:668px;height:115px;background:var(--lavender)}
.toplinks{position:absolute;left:26px;top:17px;font-size:7px;font-weight:700;color:var(--white);display:flex;align-items:center;gap:5px;letter-spacing:.2px}
.brand{position:absolute;left:30px;top:50px;display:flex;align-items:center;gap:7px}
.brand-dot{width:14px;height:14px;border-radius:50%;background:var(--pink)}
.brand-name{font-family:"Pacifico",cursive;font-size:20px;color:var(--pink);line-height:1}
.lang{position:absolute;left:542px;top:37px;display:flex;height:21px}
.lang .lock{width:25px;background:var(--coral);display:flex;align-items:center;justify-content:center}
.lang .en{width:39px;background:var(--lavender-dark);color:var(--white);font-size:8px;font-weight:700;display:flex;align-items:center;justify-content:center;gap:6px}
.lang .cur{width:33px;margin-left:2px;background:var(--white);color:var(--lavender);font-size:8px;font-weight:700;display:flex;align-items:center;justify-content:center;gap:5px}
.search{position:absolute;left:332px;top:75px;display:flex;height:22px;border:1px solid var(--white)}
.search .field{width:111px}
.search .btn{width:51px;border-left:1px solid var(--white);color:var(--white);font-size:7px;font-weight:700;display:flex;align-items:center;justify-content:center}
.cart{position:absolute;left:527px;top:75px;display:flex;height:22px;border:1px solid var(--white);color:var(--white);font-size:7px;font-weight:700}
.cart .label{width:47px;display:flex;align-items:center;justify-content:center;gap:3px;border-right:1px solid var(--white)}
.cart .state{width:64px;display:flex;align-items:center;justify-content:space-between;padding:0 9px 0 10px}

/* navigation */
.nav{position:absolute;left:0;top:115px;width:668px;height:39px;background:var(--coral);display:flex;justify-content:space-between;align-items:center;padding:0 26px 0 26px}
.nav a{color:var(--white);font-size:8.5px;font-weight:700;text-decoration:none;letter-spacing:.2px}

/* hero */
.hero{position:absolute;left:0;top:154px;width:668px;height:254px;display:flex}
.hero-photo{height:100%}
.photo-hat{width:220px;background:linear-gradient(135deg,#f6bfd0,#f7d5cc 55%,#e8a5b8)}
.photo-crowns{width:215px;background:linear-gradient(180deg,#f4fbfd,#ffffff 50%,#fde6ee)}
.photo-sleep{width:233px;background:linear-gradient(160deg,#f8f8f8,#efd9cc 60%,#d8c1ae)}
.promo{position:absolute;left:0;top:408px;width:668px;height:25px;display:flex}
.promo-look{width:220px;background:var(--pink);color:var(--white);font-family:"Pacifico",cursive;font-size:14px;display:flex;align-items:center;padding-left:12px;gap:8px}
.promo-look .arrow{margin-left:auto;margin-right:10px;font-family:"Open Sans",sans-serif;font-weight:700;font-size:13px}
.promo-sale{flex:1;background:var(--sky);color:var(--white);font-size:12px;font-weight:600;display:flex;align-items:center;padding-left:16px;position:relative}
.promo-enter{position:absolute;right:0;top:0;height:25px;width:145px;background:var(--sky-light);border-radius:14px 0 0 14px;display:flex;align-items:center;padding-left:12px;font-size:12px;font-weight:600}

/* showcase */
.showcase{position:absolute;left:24px;top:454px;width:620px;display:flex;justify-content:space-between}
.showcase-item{width:142px}
.showcase-photo{height:107px;border-radius:4px}
.showcase-label{margin-top:14px;height:62px;display:flex;flex-direction:column;align-items:center;justify-content:center;font-family:"Pacifico",cursive;color:var(--white);line-height:1.15}
.showcase-label .name{font-size:14px}
.showcase-label .price{font-size:13px}
.tone-green{background:var(--green)} .tone-green .price{color:#e3f7a0}
.tone-yellow{background:var(--yellow)} .tone-yellow .price{color:#fff3c4}
.tone-red{background:var(--red)} .tone-red .price{color:#f9a4b0}
.tone-teal{background:var(--teal)} .tone-teal .price{color:#b8ecf6}

.fill-pink{background:radial-gradient(ellipse at center,#e8336d 0%,#f27aa0 45%,#fff 72%)}
.fill-blue{background:radial-gradient(ellipse at center,#39c7d3 0%,#8fe0e6 45%,#fff 72%)}
.fill-navy{background:radial-gradient(ellipse at center,#3a4a6b 0%,#8e9bb5 45%,#fff 72%)}
.fill-brown{background:radial-gradient(ellipse at center,#6e5d52 0%,#b5a79c 45%,#fff 72%)}

/* featured */
.featured-title{position:absolute;left:0;top:660px;width:668px;text-align:center;font-family:"Pacifico",cursive;font-size:16px;color:var(--sky-text)}
.featured-rule{position:absolute;left:26px;top:695px;width:616px;border-top:1px dashed var(--sky-text)}
.featured{position:absolute;left:26px;top:717px;width:616px;display:flex;justify-content:space-between}
.card{width:142px;text-align:center}
.card-photo{height:137px;border:1px solid var(--line);padding:14px}
.card-photo div{width:100%;height:100%}
.card-name{margin-top:12px;font-size:6.5px;color:var(--red)}
.card-text{margin-top:3px;font-size:6.5px;font-weight:600;color:var(--ink);white-space:nowrap}
.card-cart{margin-top:7px;display:flex;justify-content:center}

/* footer */
.footer{position:absolute;left:0;top:941px;width:668px;height:215px;background:var(--sky);color:var(--white)}
.footer-col{position:absolute;top:36px;width:142px}
.footer-col h3{font-family:"Pacifico",cursive;font-weight:400;font-size:15px;height:26px}
.footer-col .rule{border-top:1px dashed #cfe5f2;margin-top:4px}
.footer-col ul{list-style:none;margin-top:23px}
.footer-col li{font-size:7px;font-weight:600;line-height:14.8px}
.social{display:flex;gap:10px;margin-top:28px}
.social span{width:23px;height:23px;border-radius:50%;background:#9ac7e2}
.contact .addr{margin-top:24px;font-size:7px;font-weight:700}
.contact .phone{margin-top:13px;font-size:13px;font-weight:600;color:#cde5f3}
.contact .mail{margin-top:7px;font-size:8px;display:flex;align-items:center;gap:5px}
</style>
</head>
<body>
<div class="page">
  <header class="header">
    <div class="toplinks">
      <svg width="9" height="8" viewBox="0 0 9 8"><path d="M4.5 0 0 4h1.2v4h2.3V5.5h2V8h2.3V4H9z" fill="#fff"/></svg>
      <span>CONTACT</span><span>·</span><span>SITEMAP</span>
    </div>
    <div class="brand"><span class="brand-dot"></span><span class="brand-name">Honeyvale Stitchery</span></div>
    <div class="lang">
      <div class="lock"><svg width="9" height="11" viewBox="0 0 9 11"><path d="M2 5V3.3a2.5 2.5 0 0 1 5 0V5" stroke="#fff" stroke-width="1.4" fill="none"/><rect x="0.5" y="5" width="8" height="6" rx="1" fill="#fff"/></svg></div>
      <div class="en">En <span>⌄</span></div>
      <div class="cur">$ <span>⌄</span></div>
    </div>
    <div class="search"><div class="field"></div><div class="btn">SEARCH</div></div>
    <div class="cart">
      <div class="label"><svg width="9" height="8" viewBox="0 0 9 8"><path d="M0 .5h1.5l1.2 5h5L9 2H2.2" stroke="#fff" stroke-width="1" fill="none"/><circle cx="3.2" cy="7.2" r=".8" fill="#fff"/><circle cx="7" cy="7.2" r=".8" fill="#fff"/></svg>CART</div>
      <div class="state"><span>(empty)</span><span>⌄</span></div>
    </div>
  </header>

  <nav class="nav">
    <a>SETS</a><a>ONE PIECE</a><a>DRESSES</a><a>BODYSUITS</a><a>TOPS</a><a>BOTTOMS</a><a>OUTERWEAR</a><a>PAJAMAS</a><a>COSTUMES</a><a>SWIMWEAR</a>
  </nav>

  <section class="hero">
    <div class="hero-photo photo-hat" role="img" aria-label="Baby wearing a pink crochet hat with a flower"></div>
    <div class="hero-photo photo-crowns" role="img" aria-label="Blue and pink crochet crowns"></div>
    <div class="hero-photo photo-sleep" role="img" aria-label="Sleeping newborn wearing a blue crochet crown"></div>
  </section>
  <div class="promo">
    <div class="promo-look">Complete Her Look<span class="arrow">›</span></div>
    <div class="promo-sale">TAKE AN EXTRA 50% OFF CLEARANCE PRICES
      <div class="promo-enter">› ENTER SHOP</div>
    </div>
  </div>

  <section class="showcase">
    <div class="showcase-item">
      <div class="showcase-photo fill-pink" role="img" aria-label="Pink crochet crown"></div>
      <div class="showcase-label tone-green"><span class="name">Pink Crown</span><span class="price">from $2.50</span></div>
    </div>
    <div class="showcase-item">
      <div class="showcase-photo fill-blue" role="img" aria-label="Blue crochet crown"></div>
      <div class="showcase-label tone-yellow"><span class="name">Blue Crown</span><span class="price">from $5.00</span></div>
    </div>
    <div class="showcase-item">
      <div class="showcase-photo fill-navy" role="img" aria-label="Navy crochet baby sneakers with red stars"></div>
      <div class="showcase-label tone-red"><span class="name">Starlet Booties</span><span class="price">from $20</span></div>
    </div>
    <div class="showcase-item">
      <div class="showcase-photo fill-brown" role="img" aria-label="Brown crochet baby sneakers with pink stars"></div>
      <div class="showcase-label tone-teal"><span class="name">Pebble Booties</span><span class="price">from $18.00</span></div>
    </div>
  </section>

  <h2 class="featured-title">Featured products</h2>
  <div class="featured-rule"></div>
  <section class="featured">
    <div class="card">
      <div class="card-photo"><div class="fill-pink" role="img" aria-label="Pink crochet crown"></div></div>
      <div class="card-name">Kerouyas Jertyas®</div>
      <div class="card-text">Lorem ipsum dolor sit amet, consectetur...</div>
      <div class="card-cart"><svg width="12" height="11" viewBox="0 0 12 11"><path d="M0 1h2l1.6 6.2h6.4L11.5 3H2.8" stroke="#8cc8ec" stroke-width="1.3" fill="none"/><circle cx="4.3" cy="9.6" r="1" fill="#8cc8ec"/><circle cx="9.2" cy="9.6" r="1" fill="#8cc8ec"/></svg></div>
    </div>
    <div class="card">
      <div class="card-photo"><div class="fill-blue" role="img" aria-label="Blue crochet crown"></div></div>
      <div class="card-name">Miuyas Laytsas®</div>
      <div class="card-text">Lorem ipsum dolor sit amet, consectetur...</div>
      <div class="card-cart"><svg width="12" height="11" viewBox="0 0 12 11"><path d="M0 1h2l1.6 6.2h6.4L11.5 3H2.8" stroke="#8cc8ec" stroke-width="1.3" fill="none"/><circle cx="4.3" cy="9.6" r="1" fill="#8cc8ec"/><circle cx="9.2" cy="9.6" r="1" fill="#8cc8ec"/></svg></div>
    </div>
    <div class="card">
      <div class="card-photo"><div class="fill-navy" role="img" aria-label="Navy crochet baby sneakers"></div></div>
      <div class="card-name">Dolore Vertyuasa®</div>
      <div class="card-text">Lorem ipsum dolor sit amet, consectetur...</div>
      <div class="card-cart"><svg width="12" height="11" viewBox="0 0 12 11"><path d="M0 1h2l1.6 6.2h6.4L11.5 3H2.8" stroke="#8cc8ec" stroke-width="1.3" fill="none"/><circle cx="4.3" cy="9.6" r="1" fill="#8cc8ec"/><circle cx="9.2" cy="9.6" r="1" fill="#8cc8ec"/></svg></div>
    </div>
    <div class="card">
      <div class="card-photo"><div class="fill-brown" role="img" aria-label="Brown crochet baby sneakers"></div></div>
      <div class="card-name">Serthbytas Nutras®</div>
      <div class="card-text">Lorem ipsum dolor sit amet, consectetur...</div>
      <div class="card-cart"><svg width="12" height="11" viewBox="0 0 12 11"><path d="M0 1h2l1.6 6.2h6.4L11.5 3H2.8" stroke="#8cc8ec" stroke-width="1.3" fill="none"/><circle cx="4.3" cy="9.6" r="1" fill="#8cc8ec"/><circle cx="9.2" cy="9.6" r="1" fill="#8cc8ec"/></svg></div>
    </div>
  </section>

  <footer class="footer">
    <div class="footer-col" style="left:26px">
      <h3>follow us</h3><div class="rule"></div>
      <div class="social"><span></span><span></span><span></span></div>
    </div>
    <div class="footer-col" style="left:184px">
      <h3>information</h3><div class="rule"></div>
      <ul><li>SPECIALS</li><li>BEST SELLERS</li><li>CONTACT US</li><li>TERMS AND CONDITIONS OF USE</li><li>SITEMAP</li></ul>
    </div>
    <div class="footer-col" style="left:342px">
      <h3>my account</h3><div class="rule"></div>
      <ul><li>MY ORDERS</li><li>MY CREDIT SLIPS</li><li>MY ADDRESSES</li><li>MY PERSONAL INFO</li><li>MY FAVORITE PRODUCTS.</li></ul>
    </div>
    <div class="footer-col contact" style="left:500px">
      <h3>contact us</h3><div class="rule"></div>
      <div class="addr">COMPANY ADRESS</div>
      <div class="phone">0(000) 000-0000</div>
      <div class="mail"><svg width="10" height="7" viewBox="0 0 10 7"><rect x=".5" y=".5" width="9" height="6" fill="none" stroke="#cde5f3"/><path d="M.5.5 5 4 9.5.5" fill="none" stroke="#cde5f3"/></svg>hello@honeyvalemail.org</div>
    </div>
  </footer>
</div>
</body>
</html>
```